Detox Poster Design Project

I am a naturopath that works in Melbourne. I require a poster that I can put up in my natural therapies clinic that is advertising a detox program that I am offering. The program runs for 3 or 6 weeks and is designed to help your liver, gut and kidney cleanse toxins more efficiently, leaving you feeling energised and healthy.

I would like to see designs that are fresh, organic, clear and contemporary to look at. I want to sell the idea of feeling good, wellbeing and vitality to the potential client. Colours I like include greens, greys and blues.

The final design should communicate health and happiness.

Requirements
Must have
• Please include the photo of the woman in nature.Poster size will be A2 594mm by 420mm
Nice to have
• I have attached the design work for my business cards that you can use. It would be great if the colours and style are in keeping with the existing design work for my business. I have also attached an extra image (almond milk photo) just in case you could see a use for it.

Many thanks.
Should not have
• No hippy, new age looking design.

```html
<!DOCTYPE html>
<html lang="en">
<head>
<meta charset="utf-8">
<title>Detox Program – Clara Whitfield Naturopath</title>
<link rel="stylesheet" href="https://fonts.googleapis.com/css2?family=Jost:wght@200;300;400&display=swap">
<style>
  :root {
    --aqua: #1fe0cf;
    --aqua-soft: #2fd6c8;
    --aqua-deep: #0fb3a6;
    --aqua-faint: #d3f7f3;
    --paper: #ffffff;
    --haze: #f4f9ea;
    --leaf-light: #d9ecbf;
    --leaf-mid: #9fcb6c;
    --leaf-green: #6fae45;
    --leaf-deep: #417f2c;
    --leaf-dark: #2b5e1f;
    --skin-light: #f1e2c9;
  }
  * { margin: 0; padding: 0; box-sizing: border-box; }
  html, body {
    width: 776px;
    height: 1200px;
    overflow: hidden;
    background: var(--paper);
  }
  .poster {
    position: relative;
    width: 776px;
    height: 1200px;
    overflow: hidden;
    font-family: "Jost", "Helvetica Neue", Arial, sans-serif;
    background: var(--paper);
  }
  .hero-photo {
    position: absolute;
    inset: 0;
    background:
      linear-gradient(180deg, var(--paper) 0%, var(--paper) 22%, rgba(255,255,255,0.75) 30%, rgba(255,255,255,0) 44%),
      radial-gradient(ellipse 22% 20% at 52% 76%, rgba(241,226,201,0.85), rgba(241,226,201,0) 75%),
      radial-gradient(ellipse 40% 26% at 30% 45%, rgba(250,252,232,0.9), rgba(250,252,232,0) 70%),
      radial-gradient(ellipse 30% 30% at 92% 55%, rgba(226,240,170,0.8), rgba(226,240,170,0) 70%),
      radial-gradient(ellipse 35% 30% at 8% 85%, rgba(65,127,44,0.85), rgba(65,127,44,0) 75%),
      radial-gradient(ellipse 35% 30% at 95% 88%, rgba(111,174,69,0.9), rgba(111,174,69,0) 75%),
      linear-gradient(180deg,
        var(--haze) 30%,
        var(--leaf-light) 42%,
        var(--leaf-mid) 58%,
        var(--leaf-green) 74%,
        var(--leaf-deep) 90%,
        var(--leaf-dark) 100%);
  }
  .accent-circle {
    position: absolute;
    left: 540px;
    top: 60px;
    width: 180px;
    height: 180px;
    border-radius: 50%;
    background: var(--aqua-faint);
    opacity: 0.85;
  }
  .headline {
    position: absolute;
    left: 46px;
    top: 34px;
    color: var(--aqua);
    font-weight: 200;
    line-height: 1;
  }
  .headline__main {
    display: block;
    font-size: 152px;
    letter-spacing: -1px;
  }
  .headline__sub {
    display: block;
    margin-top: -12px;
    margin-left: 2px;
    font-size: 96px;
    letter-spacing: 0.5px;
  }
  .intro {
    position: absolute;
    left: 52px;
    top: 280px;
    width: 500px;
    color: var(--aqua-soft);
    font-size: 21.5px;
    font-weight: 300;
    line-height: 31px;
  }
  .brand-band {
    position: absolute;
    left: 0;
    top: 1048px;
    width: 776px;
    height: 110px;
    background: rgba(255,255,255,0.8);
    display: flex;
    align-items: center;
    justify-content: center;
    gap: 12px;
  }
  .brand-band__mark {
    width: 52px;
    height: 52px;
    border-radius: 50%;
    background: var(--aqua);
  }
  .brand-band__name {
    color: var(--aqua-deep);
    font-weight: 300;
    line-height: 1;
  }
  .brand-band__person {
    display: block;
    font-size: 34px;
  }
  .brand-band__role {
    display: block;
    margin-top: 4px;
    font-size: 19px;
    letter-spacing: 0.3px;
  }
</style>
</head>
<body>
  <main class="poster">
    <div class="hero-photo" role="img" aria-label="Woman seen from behind with a braided ponytail, arms raised joyfully in a sunlit lush green tropical garden"></div>
    <div class="accent-circle" aria-hidden="true"></div>

    <h1 class="headline">
      <span class="headline__main">DETOX</span>
      <span class="headline__sub">PROGRAM</span>
    </h1>

    <p class="intro">
      Designed to help your liver,<br>
      gut and kidney cleanse toxins more efficiently,<br>
      leaving you feeling energised and healthy.<br>
      Runs for 3 or 6 weeks.
    </p>

    <footer class="brand-band">
      <span class="brand-band__mark" aria-hidden="true"></span>
      <span class="brand-band__name">
        <span class="brand-band__person">Clara Whitfield</span>
        <span class="brand-band__role">NATUROPATH</span>
      </span>
    </footer>
  </main>
</body>
</html>
```